Byte Lantern Website

Design and implement (fully coded and ready to launch) website for a professional services company - please see the documents attached and send us an email if there are any questions
Target Market(s)
Market to potential clients about the services we offer and be able to reach us for any consulting opportunities
Industry/Entity Type
Professional Service
Coding
Coded - Design and coding required
Number of Pages Required
3 page
Requirements
Must have
- Single page website design that is SEO optimized
Blog Post
Contact US page
Cool images/ logos for the service offering - not fill the website with text/content
Must be professional looking website
Coded website should also look great on different screens - mobile, tablets etc
Nice to have
- Choose easy neutral colors that compliment the logo colors. Having said that don't use every color in the logo for the website design.
Should not have
- Too many colors and several various different fonts

```html
<!DOCTYPE html>
<html lang="en">
<head>
<meta charset="utf-8">
<title>Byte Lantern</title>
<link rel="stylesheet" href="https://fonts.googleapis.com/css2?family=Montserrat:wght@400;500;600;700&display=swap">
<style>
:root{
  --ink:#222629;
  --text:#3f4346;
  --accent:#f0552b;
  --accent-2:#e8342f;
  --dark:#24272b;
  --light:#e9eaec;
  --white:#ffffff;
  --red-panel:#ec3f3a;
}
*{box-sizing:border-box;margin:0;padding:0}
html,body{width:1200px;height:4042px;overflow:hidden}
body{position:relative;font-family:"Montserrat",sans-serif;color:var(--text);background:var(--white)}

/* header */
.site-header{position:absolute;left:0;top:0;width:1200px;height:125px;background:var(--white)}
.brand{position:absolute;left:117px;top:46px;font-weight:600;font-size:29px;letter-spacing:1px;color:var(--ink)}
.nav a{position:absolute;top:56px;font-size:15.5px;font-weight:500;color:var(--ink);text-decoration:none;white-space:nowrap}
.nav a.active{color:var(--accent)}

/* hero */
.hero{position:absolute;left:0;top:125px;width:1200px;height:550px;
  background:linear-gradient(100deg,#0b2f63 0%,#0f5a8e 40%,#138aa8 70%,#1ab3c3 100%)}
.hero-art{position:absolute;left:40px;top:20px;width:520px;height:500px;border-radius:8px;
  background:radial-gradient(ellipse at 50% 45%,rgba(40,210,220,.45),rgba(20,60,120,0) 70%)}
.hero-title{position:absolute;right:108px;top:200px;text-align:right;color:var(--white);font-weight:700;font-size:64px;letter-spacing:2px;line-height:1}
.hero-title small{display:block;font-size:24px;font-weight:500;margin-top:4px;letter-spacing:1px}
.dots{position:absolute;left:578px;top:512px;display:flex;gap:6px}
.dots span{width:10px;height:10px;border-radius:50%;background:var(--white)}
.dots span.on{background:var(--accent-2)}

/* headings */
.section-title{position:absolute;font-weight:600;font-size:38px;letter-spacing:1px;color:var(--ink);white-space:nowrap}
.center{left:0;width:1200px;text-align:center}

/* about */
.about-body{position:absolute;left:111px;top:843px;width:585px}
.about-text{font-size:15px;line-height:36px;color:var(--text);hyphens:auto;-webkit-hyphens:auto}
.about-photo{position:absolute;left:723px;top:819px;width:369px;height:314px;
  background:linear-gradient(135deg,#c9d6e2,#7c93a8 55%,#3b4d5f)}
.btn{height:50px;border-radius:25px;background:linear-gradient(90deg,var(--accent),var(--accent-2));
  color:var(--white);font-weight:700;font-size:17px;letter-spacing:.5px;display:flex;align-items:center;justify-content:center}
.about-body .btn{width:154px;margin-top:12px}

/* services */
.services{position:absolute;left:0;top:1231px;width:1200px;height:562px;background:linear-gradient(180deg,#2b2e33,#1f2226)}
.services .section-title{color:var(--white);top:70px}
.service{position:absolute;top:177px;width:320px;text-align:center;color:var(--white)}
.service-icon{width:120px;height:120px;border-radius:50%;margin:0 auto;
  background:linear-gradient(135deg,#f47a3a,var(--accent-2));display:flex;align-items:center;justify-content:center}
.service h3{font-size:22px;font-weight:600;margin-top:26px}
.service p{width:260px;margin:14px auto 0;font-size:14.5px;line-height:33px;color:#e6e6e6}
.divider{position:absolute;top:248px;width:1px;height:270px;background:#cfd2d6}

/* technology */
.tile{position:absolute;width:118px;height:118px;transform:rotate(45deg);border-radius:14px;background:var(--white);
  border:1px solid #f7d0cf;box-shadow:0 3px 10px rgba(240,85,43,.14)}
.tile-label{position:absolute;width:160px;text-align:center;font-weight:600;font-size:15px;color:#2d5f8f;line-height:1.2}

/* blog */
.blog{position:absolute;left:0;top:2366px;width:1200px;height:622px;background:linear-gradient(180deg,#e7e8ea,#eef0f2)}
.blog-card{position:absolute;top:181px;width:300px}
.blog-img{height:201px;background:linear-gradient(135deg,#2f3b48,#5b6a78 60%,#9aa6b0)}
.blog-meta{position:relative;margin-top:52px;padding-left:32px;border-left:3px solid #3b3e42;height:115px}
.blog-date{display:flex;align-items:center;gap:12px;font-size:18px;color:var(--ink)}
.blog-meta p{font-size:13.5px;line-height:24px;margin-top:14px;color:var(--text)}

/* profile */
.bio-body{position:absolute;left:110px;top:3160px;width:556px}
.bio{font-size:15.5px;line-height:36px;text-align:justify;hyphens:auto;-webkit-hyphens:auto}
.bio-body .btn{width:152px;margin-top:18px}
.red-panel{position:absolute;left:780px;top:3134px;width:310px;height:306px;background:var(--red-panel)}
.red-panel .line{position:absolute;left:196px;width:1px;background:rgba(255,255,255,.8)}
.profile-photo{position:absolute;left:717px;top:3187px;width:201px;height:200px;border:1px solid #fff;
  background:linear-gradient(160deg,#8a6d55,#5a4a3e 60%,#b9b8c4)}
.social{position:absolute;left:961px;width:33px;height:33px;border-radius:50%;border:2px solid var(--white)}

/* footer */
.site-footer{position:absolute;left:0;top:3595px;width:1200px;height:447px;background:#3a3c3f;color:var(--white)}
.footer-brand{position:absolute;left:0;width:1200px;top:100px;text-align:center;font-weight:600;font-size:30px;letter-spacing:1px}
.contact-icon{position:absolute;top:179px;width:62px;height:62px;border-radius:50%;background:var(--white);display:flex;align-items:center;justify-content:center}
.contact-text{position:absolute;top:260px;width:300px;text-align:center;font-size:18px;line-height:32px}
.copy{position:absolute;left:110px;top:390px;width:980px;display:flex;align-items:center;gap:10px;font-size:15px}
.copy span.rule{flex:1;height:1px;background:#bfc1c3}
</style>
</head>
<body>

<header class="site-header">
  <div class="brand">BYTE LANTERN</div>
  <nav class="nav">
    <a class="active" style="left:414px">HOME</a>
    <a style="left:502px">OUR SERVICES</a>
    <a style="left:654px">ABOUT US</a>
    <a style="left:774px">CAREERS</a>
    <a style="left:882px">RESOURCES</a>
    <a style="left:1015px">CONTACT</a>
  </nav>
</header>

<section class="hero">
  <div class="hero-art" role="img" aria-label="Glowing laptop with floating data charts and connected network icons"></div>
  <h1 class="hero-title">BYTE LANTERN<small>LLC</small></h1>
  <div class="dots"><span></span><span class="on"></span><span></span></div>
</section>

<section>
  <h2 class="section-title" style="left:111px;top:772px">ABOUT US</h2>
  <div class="about-body">
    <p class="about-text">Lorem ipsum dolor sit amet, consectetur adipiscing elit, sed do eiusmod tempor incididunt ut labore et dolore magna aliqua. Quis ipsum suspendisse ultrices gravida. Risus commodo viverra maecenas accumsan lacus vel facilisis. Lorem ipsum dolor sit amet, consectetur adipiscing elit, sed do eiusmod tempor incididunt ut labore et dolore magna aliqua. Quis ipsum suspendisse ultrices gravida. Risus commodo viverra maecenas accumsan lacus vel facilisis. Lorem ipsum dolor sit amet,</p>
    <div class="btn">READ MORE</div>
  </div>
  <div class="about-photo" role="img" aria-label="Two colleagues reviewing work together on a computer monitor"></div>
</section>

<section class="services">
  <h2 class="section-title center">OUR SERVICES</h2>
  <div class="service" style="left:98px">
    <div class="service-icon"><svg width="60" height="60" viewBox="0 0 60 60" fill="none" stroke="#fff" stroke-width="2.5"><rect x="10" y="12" width="36" height="36" rx="2"/><path d="M18 40 L42 16 M38 14 l6 6"/><path d="M14 48 h34 v-10"/></svg></div>
    <h3>Platform Architecture</h3>
    <p>Byte Lantern works very closely with clients, product managers to understand the scope ofthe requirements, discuss myriad</p>
  </div>
  <div class="divider" style="left:444px"></div>
  <div class="service" style="left:439px;top:175px">
    <div class="service-icon"><svg width="60" height="60" viewBox="0 0 60 60" fill="none" stroke="#fff" stroke-width="2.5"><rect x="10" y="14" width="22" height="34" rx="2"/><path d="M15 22h12M15 29h12M15 36h8"/><circle cx="42" cy="22" r="7"/><circle cx="42" cy="40" r="6"/></svg></div>
    <h3>Data Engineering</h3>
    <p>Byte Lantern employs the latest proven technologies, best practices, industry standards in building the Data Lakes that has</p>
  </div>
  <div class="divider" style="left:786px"></div>
  <div class="service" style="left:792px">
    <div class="service-icon"><svg width="60" height="60" viewBox="0 0 60 60" fill="none" stroke="#fff" stroke-width="2.5"><circle cx="30" cy="30" r="20"/><path d="M20 40V32M27 40V26M34 40V22M41 40V18"/></svg></div>
    <h3>Cloud Developments</h3>
    <p>Byte Lantern employs the latest proven technologies, best practices, industry standards in building the Data Lakes that has</p>
  </div>
</section>

<section>
  <h2 class="section-title center" style="top:1886px">OUR TECHNOLOGY</h2>
  <div class="tile" style="left:172px;top:2015px"></div><div class="tile-label" style="left:151px;top:2065px">Harrowfield</div>
  <div class="tile" style="left:363px;top:2015px"></div><div class="tile-label" style="left:342px;top:2065px">Emberline</div>
  <div class="tile" style="left:545px;top:2015px"></div><div class="tile-label" style="left:524px;top:2065px">Quillstream</div>
  <div class="tile" style="left:730px;top:2015px"></div><div class="tile-label" style="left:709px;top:2065px">Tidepool</div>
  <div class="tile" style="left:909px;top:2015px"></div><div class="tile-label" style="left:888px;top:2065px">Frostgrid</div>
  <div class="tile" style="left:267px;top:2131px"></div><div class="tile-label" style="left:246px;top:2172px">Northwind<br>Cloud</div>
  <div class="tile" style="left:452px;top:2131px"></div><div class="tile-label" style="left:431px;top:2181px">Skyvault</div>
  <div class="tile" style="left:636px;top:2131px"></div><div class="tile-label" style="left:615px;top:2181px">Flowmason</div>
  <div class="tile" style="left:822px;top:2131px"></div><div class="tile-label" style="left:801px;top:2181px">Taskhive</div>
</section>

<section class="blog">
  <h2 class="section-title center" style="top:77px">LATEST BLOG</h2>
  <article class="blog-card" style="left:119px">
    <div class="blog-img" role="img" aria-label="Developer working at multiple code screens"></div>
    <div class="blog-meta">
      <div class="blog-date"><svg width="30" height="28" viewBox="0 0 30 28" fill="none" stroke="#3b3e42" stroke-width="1.6"><rect x="2" y="4" width="26" height="22"/><path d="M2 10h26M8 1v6M22 1v6M8 15h3M14 15h3M20 15h3M8 20h3M14 20h3"/></svg>March 10,2020</div>
      <p>Lorem ipsum dolor sit amet, consectetur adipiscing elit, sed do eiusmod tempor incididunt</p>
    </div>
  </article>
  <article class="blog-card" style="left:458px">
    <div class="blog-img" role="img" aria-label="Team discussing code on a large monitor"></div>
    <div class="blog-meta">
      <div class="blog-date"><svg width="30" height="28" viewBox="0 0 30 28" fill="none" stroke="#3b3e42" stroke-width="1.6"><rect x="2" y="4" width="26" height="22"/><path d="M2 10h26M8 1v6M22 1v6M8 15h3M14 15h3M20 15h3M8 20h3M14 20h3"/></svg>March 10,2020</div>
      <p>Lorem ipsum dolor sit amet, consectetur adipiscing elit, sed do eiusmod tempor incididunt</p>
    </div>
  </article>
  <article class="blog-card" style="left:798px">
    <div class="blog-img" role="img" aria-label="Hands typing on a keyboard in front of code screens" style="background:linear-gradient(135deg,#dfe3e6,#9aa4ad 55%,#3a4650)"></div>
    <div class="blog-meta">
      <div class="blog-date"><svg width="30" height="28" viewBox="0 0 30 28" fill="none" stroke="#3b3e42" stroke-width="1.6"><rect x="2" y="4" width="26" height="22"/><path d="M2 10h26M8 1v6M22 1v6M8 15h3M14 15h3M20 15h3M8 20h3M14 20h3"/></svg>March 10,2020</div>
      <p>Lorem ipsum dolor sit amet, consectetur adipiscing elit, sed do eiusmod tempor incididunt</p>
    </div>
  </article>
</section>

<section>
  <h2 class="section-title" style="left:110px;top:3080px">ARUN VEDAM</h2>
  <div class="bio-body">
    <p class="bio">Arun manages all the client interactions and engineering team at Byte Lantern. Arun has over15 years of experience in the technology before he founded Byte Lantern. He managed development of large scale enterprise wide, high performance, scalable, real-time software solutions in Tele-communications, Gaming, Finance, and Insurance Industries.He spends time working on open source projects, contributions to Riverstone Ledger.</p>
    <div class="btn">READ MORE</div>
  </div>
  <div class="red-panel">
    <div class="line" style="top:0;height:80px"></div>
    <div class="line" style="top:230px;height:76px"></div>
  </div>
  <div class="profile-photo" role="img" aria-label="Portrait photo of Arun Vedam"></div>
  <div class="social" style="top:3224px" aria-label="Social profile"></div>
  <div class="social" style="top:3276px" aria-label="Social profile"></div>
  <div class="social" style="top:3326px" aria-label="Social profile"></div>
</section>

<footer class="site-footer">
  <div class="footer-brand">BYTE LANTERN</div>
  <div class="contact-icon" style="left:261px"><svg width="26" height="26" viewBox="0 0 24 24" fill="#222629"><path d="M6.6 10.8a15.1 15.1 0 0 0 6.6 6.6l2.2-2.2a1 1 0 0 1 1-.25 11.4 11.4 0 0 0 3.6.57 1 1 0 0 1 1 1V20a1 1 0 0 1-1 1A17 17 0 0 1 3 4a1 1 0 0 1 1-1h3.5a1 1 0 0 1 1 1c0 1.25.2 2.45.57 3.6a1 1 0 0 1-.25 1z"/></svg></div>
  <div class="contact-icon" style="left:545px"><svg width="22" height="26" viewBox="0 0 24 28" fill="#222629"><path d="M12 1a9 9 0 0 0-9 9c0 7 9 17 9 17s9-10 9-17a9 9 0 0 0-9-9zm0 12.5A3.5 3.5 0 1 1 12 6.5a3.5 3.5 0 0 1 0 7z"/></svg></div>
  <div class="contact-icon" style="left:844px"><svg width="24" height="18" viewBox="0 0 24 18" fill="#222629"><path d="M1 1h22v16H1z"/><path d="M1 1l11 9 11-9" fill="none" stroke="#fff" stroke-width="1.6"/></svg></div>
  <div class="contact-text" style="left:142px">555-014-2290</div>
  <div class="contact-text" style="left:426px">Harbor Showroom ,<br>48 Elm Street<br>Lakeview, MA</div>
  <div class="contact-text" style="left:725px">info@bytelantern.com</div>
  <div class="copy"><span class="rule"></span>Copyrights 2020. All rights reserved<span class="rule"></span></div>
</footer>

</body>
</html>
```